brightmesh Business Card

Already have the logo, but now need the business card design

Industry/Entity Type

Business Software

Contact Information for Business Card

web site will be brightmesh.io / The card should have the person name / position / mobile / email / and company address

Colors

Designer to choose colors to be used in the design.

Requirements
Must have
• See business card details
• One side to have the brightmesh logo
Nice to have
• If possible the 'O' from flow can be watermarked into the second side
• Try to fit in the words brightmesh Business Solutions

```html
<!DOCTYPE html>
<html lang="en">
<head>
<meta charset="utf-8">
<title>brightmesh Business Card</title>
<link href="https://fonts.googleapis.com/css2?family=Roboto:ital,wght@0,400;0,500;1,400&display=swap" rel="stylesheet">
<style>
  :root {
    --backdrop: #3b3b3d;
    --card: #151516;
    --card-edge: #222224;
    --gloss: #2c2c2f;
    --white: #f2f2f2;
    --muted: #c9c9c9;
    --accent: #d8232a;
  }
  * { box-sizing: border-box; margin: 0; padding: 0; }
  html, body { width: 800px; height: 1200px; overflow: hidden; }
  body {
    background: var(--backdrop);
    font-family: "Roboto", Arial, sans-serif;
    position: relative;
  }
  .card {
    position: absolute;
    left: 80px;
    width: 640px;
    height: 366px;
    background: var(--card);
    border: 1px solid var(--card-edge);
    box-shadow: 0 18px 40px rgba(0,0,0,0.45);
  }
  .card--front { top: 150px; }
  .card--back { top: 690px; }

  /* Shared name block */
  .brand-name {
    display: flex;
    align-items: center;
    gap: 12px;
    font-weight: 500;
    line-height: 1;
  }
  .brand-name__mark { flex: none; }
  .brand-line {
    font-size: 14px;
    font-weight: 400;
    line-height: 1.3;
  }

  /* Front */
  .front-brand {
    position: absolute;
    left: 0; right: 0; top: 138px;
    display: flex;
    flex-direction: column;
    align-items: center;
  }
  .front-brand .brand-name {
    font-size: 56px;
    color: var(--gloss);
  }
  .front-brand .brand-name__mark {
    width: 18px; height: 18px;
    background: var(--gloss);
  }
  .front-brand .brand-line {
    margin-top: 14px;
    color: var(--gloss);
  }

  /* Back */
  .back-brand {
    position: absolute;
    left: 40px; top: 150px;
    width: 250px;
  }
  .back-brand .brand-name {
    font-size: 38px;
    color: var(--white);
  }
  .back-brand .brand-name__mark {
    width: 12px; height: 12px;
    background: var(--accent);
  }
  .back-brand .brand-line {
    margin-top: 10px;
    padding-left: 24px;
    font-size: 12px;
    color: var(--muted);
  }
  .divider {
    position: absolute;
    left: 320px; top: 70px;
    width: 2px; height: 226px;
    background: var(--accent);
  }
  .contact {
    position: absolute;
    left: 348px; top: 78px;
    width: 260px;
    color: var(--muted);
  }
  .contact__name {
    font-size: 24px;
    font-weight: 500;
    color: var(--accent);
  }
  .contact__role {
    font-size: 13px;
    font-style: italic;
    color: var(--white);
    margin-top: 2px;
  }
  .contact__address {
    margin-top: 22px;
    font-size: 13px;
    line-height: 1.45;
  }
  .contact__list {
    list-style: none;
    margin-top: 16px;
    font-size: 13px;
  }
  .contact__item {
    display: flex;
    align-items: center;
    gap: 10px;
    margin-bottom: 8px;
  }
  .contact__icon { width: 12px; height: 12px; flex: none; }
</style>
</head>
<body>

  <section class="card card--front" aria-label="Card front">
    <div class="front-brand">
      <div class="brand-name"><span class="brand-name__mark"></span>brightmesh</div>
      <div class="brand-line">brightmesh Business Solutions</div>
    </div>
  </section>

  <section class="card card--back" aria-label="Card back">
    <div class="back-brand">
      <div class="brand-name"><span class="brand-name__mark"></span>brightmesh</div>
      <div class="brand-line">Business Solutions</div>
    </div>

    <div class="divider"></div>

    <div class="contact">
      <div class="contact__name">Daniel Reyes</div>
      <div class="contact__role">Administrator</div>
      <div class="contact__address">1234, Any Street, Any Town,<br>Any City, Country 0000</div>
      <ul class="contact__list">
        <li class="contact__item">
          <svg class="contact__icon" viewBox="0 0 12 12" aria-hidden="true"><path d="M2.5 1h2l1 3-1.3 1a6 6 0 0 0 2.8 2.8L8 6.5l3 1v2c0 .8-.7 1.5-1.5 1.5A8.5 8.5 0 0 1 1 2.5C1 1.7 1.7 1 2.5 1z" fill="var(--accent)"/></svg>
          <span>555 014 2387</span>
        </li>
        <li class="contact__item">
          <svg class="contact__icon" viewBox="0 0 12 12" aria-hidden="true"><rect x="0.5" y="2" width="11" height="8" rx="1" fill="var(--accent)"/><path d="M1 2.8 6 6.6 11 2.8" stroke="var(--card)" stroke-width="1" fill="none"/></svg>
          <span>admin@brightmesh.io</span>
        </li>
        <li class="contact__item">
          <svg class="contact__icon" viewBox="0 0 12 12" aria-hidden="true"><circle cx="6" cy="6" r="5.2" fill="none" stroke="var(--accent)" stroke-width="1.3"/><path d="M1 6h10M6 1c-2.2 2.8-2.2 7.2 0 10M6 1c2.2 2.8 2.2 7.2 0 10" stroke="var(--accent)" stroke-width="1" fill="none"/></svg>
          <span>www.brightmesh.io</span>
        </li>
      </ul>
    </div>
  </section>

</body>
</html>
```